International research group on Amber Lantern; needs a bold, futuristic website*

We need a website and logo design for our research programme. Our research programme is about how we can build an inclusive future for our societies, at a time when there are pressures for digital technologies to be used to take away jobs and/or create precarious work. Our website is meant to provide actors in society with the latest evidence so that they can act on them to introduce new policies, programmes and activities that support human augmentation. We push our research findings through the website, as they emerge. We want the website to be futuristic and bold, but with a sense of inclusion, compassion and the preservation of human civilization in an age of machines. Pls see the uploaded file for the project brief.
Updates

Target Market(s)

• Primary: Researchers & Policy-makers
• Secondary:
a) Industry – C-suite including Chief Technology Officers, Chief Human Resource Officers
b) Practitioners – Digital consultants, jobs & skills analysts, educators, technologists, journalists

Logo Text

Amber Lantern Collective

Coding

Coded - Design and coding required

Number of Pages Required

5+ page

Font styles to use
Sans Serif

Requirements
Must have
• 1) Feature of the month
2) Repository of documents that is attractive, with highlights and easy markers for different types of stakeholders
3) Blog postings
Nice to have
• Pls see two websites we kind of like:
https://brindlequay.example/
https://www.wegstein-lorv.example/en/

```html
<!DOCTYPE html>
<html lang="en">
<head>
<meta charset="utf-8">
<title>Amber Lantern Collective</title>
<link href="https://fonts.googleapis.com/css2?family=Exo+2:wght@400;500;600;700&family=Hind:wght@400;500;600&display=swap" rel="stylesheet">
<style>
:root{
  --red:#dc0a12;
  --dark:#333333;
  --ink:#222222;
  --black:#000000;
  --soft:#f3f3f3;
  --white:#ffffff;
}
*{box-sizing:border-box;margin:0;padding:0}
html,body{width:1200px;height:3740px;overflow:hidden;background:var(--white)}
body{position:relative;font-family:"Hind",sans-serif;color:var(--ink)}
.abs{position:absolute}
h2{font-family:"Exo 2",sans-serif;font-weight:600;color:var(--red);font-size:37px;line-height:1}
p.body{font-size:14.5px;line-height:22px;color:#333}

/* header */
.brand{left:80px;top:44px;display:flex;align-items:center;gap:12px}
.brand-dot{width:38px;height:38px;border-radius:50%;background:var(--red)}
.brand-name{font-family:"Hind",sans-serif;font-weight:600;font-size:21px;color:var(--ink)}
.nav{left:389px;top:52px;display:flex;gap:36px;font-size:15px;color:#333}
.nav .on{color:var(--red);font-weight:600}

/* hero */
.hero{left:0;top:123px;width:1200px;height:690px}
.hero-photo{position:absolute;inset:0;background:radial-gradient(ellipse at 50% 35%,#8fb3c9 0%,#4f7fa3 35%,#1f4a75 75%,#122d4f 100%);clip-path:polygon(0 0,100% 0,100% 79%,50% 96%,0 79%)}
.hero-title{position:absolute;left:0;width:1200px;top:340px;text-align:center;font-family:"Exo 2",sans-serif;font-weight:600;font-size:56px;color:var(--white);text-shadow:0 2px 6px rgba(0,0,0,.35)}
.hero svg{position:absolute;left:0;top:0}

/* feature */
.feature-title{left:170px;top:905px}
.feature-text{left:170px;top:966px;width:400px}
.feature-mark{left:698px;top:860px;width:334px;height:334px;border-radius:50%;background:radial-gradient(circle at 40% 35%,#e2a2a6,#b4414a 70%,#8c2730)}

/* documents */
.docs{left:76px;top:1279px;width:1047px;height:194px;display:flex;gap:5px}
.doc{flex:1;padding:20px 40px;color:var(--white)}
.doc.red{background:var(--red)}
.doc.grey{background:var(--dark);padding-left:31px}
.doc h3{font-family:"Exo 2",sans-serif;font-size:23px;font-weight:400;margin-bottom:14px}
.doc.red h3{font-weight:600}
.doc p{font-size:14px;line-height:22px}

/* notes */
.notes-photo{left:0;top:1547px;width:602px;height:420px;background:linear-gradient(120deg,#1c2f3a 0%,#3c5a5a 40%,#c97a3e 65%,#263a44 100%)}
.notes-title{left:652px;top:1574px}
.notes-text{left:652px;top:1640px;width:410px}
.btn{left:654px;top:1893px;width:140px;height:37px;background:var(--red);color:var(--white);font-family:"Exo 2",sans-serif;font-weight:600;font-size:13px;display:flex;align-items:center;justify-content:center}

/* commentaries */
.center-title{left:0;width:1200px;text-align:center}
.quote{width:449px;height:257px;background:var(--soft);border-radius:22px;padding:34px 40px 0 58px}
.quote .mark{position:absolute;color:var(--red);font-family:"Exo 2",sans-serif;font-weight:700;font-size:22px}
.quote p{font-size:14px;line-height:22px;color:#333;width:345px}
.quote .who{font-family:"Exo 2",sans-serif;font-weight:600;font-size:19px;margin-top:12px;margin-left:8px}

/* blog */
.post-img{top:2580px;width:320px;height:213px}
.post-tag{top:2772px;width:293px;height:76px;background:var(--red);transform:skewX(-10deg);display:flex;align-items:center;justify-content:center}
.post-tag span{transform:skewX(10deg);color:var(--white);font-family:"Exo 2",sans-serif;font-weight:600;font-size:14px;line-height:17px;text-align:center;width:240px}

/* videos */
.videos{left:0;top:2913px;width:1200px;height:452px;background:var(--black)}
.thumb{top:3044px;height:272px;display:flex;align-items:center;justify-content:center}
.play{width:40px;height:40px;border-radius:50%;background:var(--red);display:flex;align-items:center;justify-content:center}

/* partners */
.partner{top:3408px;height:66px;background:#e4e4e4}
.partner.round{border-radius:50%}

/* footer */
.foot-nav{left:0;top:3532px;width:1200px;height:73px;background:var(--black);display:flex;justify-content:center;align-items:center;gap:34px;color:var(--white);font-size:15px}
.foot-nav .on{font-weight:600}
.social{top:3650px;width:28px;height:28px;background:var(--red)}
.copy{left:835px;top:3694px;font-size:15px;color:#333}
</style>
</head>
<body>

<header>
  <div class="abs brand"><span class="brand-dot"></span><span class="brand-name">Amber Lantern Collective</span></div>
  <nav class="abs nav"><span class="on">Home</span><span>About Us</span><span>Services</span><span>Practitioners</span><span>Commentaries</span><span>Blog</span><span>Video</span><span>Contact Us</span></nav>
</header>

<section class="abs hero">
  <div class="hero-photo" role="img" aria-label="Man in glasses reaching toward a glowing blue digital interface"></div>
  <svg width="1200" height="690" viewBox="0 0 1200 690" aria-hidden="true">
    <polygon points="0,545 600,662 1200,545 1200,548 600,687 0,548" fill="#dc0a12"/>
    <polyline points="586,584 596,594 606,584" fill="none" stroke="#fff" stroke-width="3"/>
  </svg>
  <div class="hero-title">Amber Lantern Collective</div>
</section>

<section>
  <h2 class="abs feature-title">Feature of the month</h2>
  <p class="abs body feature-text">Sed ut perspiciatis unde omnis iste natus error sit voluptatem accusantium doloremque laudantium, totam rem aperiam, eaque ipsa quae ab illo inventore veritatis et quasi architecto beatae vitae dicta sunt explicabo. Nemo enim ipsam voluptatem quia voluptas sit aspernatur aut odit aut fugit, sed quia consequuntur magni dolores eos qui ratione voluptatem sequi nesciunt. Neque porro quisquam est, qui dolorem ipsum quia dolor sit amet, consectetur, adipisci velit, sed quia non numquam eius modi tempora incidunt ut labore et dolore magnam aliquam quaerat voluptatem</p>
  <div class="abs feature-mark" aria-hidden="true"></div>
</section>

<section class="abs docs">
  <div class="doc red"><h3>Research reports</h3><p>Sed ut perspiciatis unde omnis iste natus error sit voluptatem accusantium doloremque laudantium, totam rem aperiam, eaque ipsa quae ab illo inventore</p></div>
  <div class="doc grey"><h3>Working papers</h3><p>Sed ut perspiciatis unde omnis iste natus error sit voluptatem accusantium doloremque laudantium, totam rem aperiam, eaque ipsa quae ab illo inventore</p></div>
  <div class="doc grey"><h3>Briefing papers</h3><p>Sed ut perspiciatis unde omnis iste natus error sit voluptatem accusantium doloremque laudantium, totam rem aperiam, eaque ipsa quae ab illo inventore</p></div>
</section>

<section>
  <div class="abs notes-photo" role="img" aria-label="Young woman in an orange beanie working on a laptop with holographic data overlays"></div>
  <h2 class="abs notes-title">Notes for practitioners</h2>
  <p class="abs body notes-text">Sed ut perspiciatis unde omnis iste natus error sit voluptatem accusantium doloremque laudantium, totam rem aperiam, eaque ipsa quae ab illo inventore veritatis et quasi architecto beatae vitae dicta sunt explicabo. Nemo enim ipsam voluptatem quia voluptas sit aspernatur aut odit aut fugit, sed quia consequuntur magni dolores eos qui ratione voluptatem sequi nesciunt. Neque porro quisquam est, qui dolorem ipsum quia dolor sit amet, consectetur, adipisci velit, sed quia non numquam eius modi tempora incidunt ut labore et dolore magnam aliquam quaerat voluptatem</p>
  <div class="abs btn">READ MORE</div>
</section>

<section>
  <h2 class="abs center-title" style="top:2066px">Commentaries</h2>
  <div class="abs quote" style="left:125px;top:2143px">
    <span class="mark" style="left:32px;top:28px">&#8220;</span>
    <p>Sed ut perspiciatis unde omnis iste natus error sit voluptatem accusantium doloremque laudantium, totam rem aperiam, eaque ipsa quae ab illo inventore veritatis et quasi architecto beatae vitae dicta sunt explicabo. Nemo enim ipsam voluptatem quia voluptas sit aspernatur aut odit aut fugit.</p>
    <span class="mark" style="left:323px;top:162px">&#8221;</span>
    <div class="who">- Dara Quill</div>
  </div>
  <div class="abs quote" style="left:604px;top:2143px">
    <span class="mark" style="left:32px;top:28px">&#8220;</span>
    <p>Sed ut perspiciatis unde omnis iste natus error sit voluptatem accusantium doloremque laudantium, totam rem aperiam, eaque ipsa quae ab illo inventore veritatis et quasi architecto beatae vitae dicta sunt explicabo. Nemo enim ipsam voluptatem quia voluptas sit aspernatur aut odit aut fugit.</p>
    <span class="mark" style="left:323px;top:162px">&#8221;</span>
    <div class="who">- Dara Quill</div>
  </div>
</section>

<section>
  <h2 class="abs center-title" style="top:2487px">Blog</h2>
  <div class="abs post-img" style="left:99px;background:linear-gradient(120deg,#2c3e55,#5d7590 50%,#1b2634)" role="img" aria-label="Woman in glasses beside server racks"></div>
  <div class="abs post-img" style="left:440px;background:linear-gradient(180deg,#8a97a3,#4c5560 60%,#23272c)" role="img" aria-label="Businessman using a smartphone in the city"></div>
  <div class="abs post-img" style="left:782px;background:linear-gradient(180deg,#0c2a6b,#1f63c2 50%,#dfe8f5)" role="img" aria-label="White humanoid robots under blue neon lights"></div>
  <div class="abs post-tag" style="left:108px"><span>Lorem ipsum dolor sit amet, consectetur adipiscing elit,</span></div>
  <div class="abs post-tag" style="left:453px"><span>Sed ut perspiciatis unde omnis iste natus error sit.</span></div>
  <div class="abs post-tag" style="left:795px"><span>Lorem ipsum dolor sit amet, consectetur adipiscing elit,</span></div>
</section>

<section class="abs videos">
  <h2 class="abs center-title" style="top:70px">Videos</h2>
</section>
<div class="abs thumb" style="left:0;width:355px;background:linear-gradient(120deg,#1d2740,#3a4a6c 50%,#151c2e)" role="img" aria-label="Two colleagues pointing at a virtual screen"><span class="play"><svg width="14" height="16" viewBox="0 0 14 16"><polygon points="2,1 13,8 2,15" fill="#fff"/></svg></span></div>
<div class="abs thumb" style="left:379px;width:439px;background:linear-gradient(110deg,#a87a52,#c9b7a8 45%,#7c8a98)" role="img" aria-label="Woman sitting on steps using a tablet with a holographic display"><span class="play"><svg width="14" height="16" viewBox="0 0 14 16"><polygon points="2,1 13,8 2,15" fill="#fff"/></svg></span></div>
<div class="abs thumb" style="left:843px;width:357px;background:linear-gradient(120deg,#2a2f38,#4a4f58 55%,#1b1e24)" role="img" aria-label="Woman working at a laptop in a dim office"><span class="play"><svg width="14" height="16" viewBox="0 0 14 16"><polygon points="2,1 13,8 2,15" fill="#fff"/></svg></span></div>

<section aria-label="Partners">
  <svg class="abs" style="left:128px;top:3428px" width="14" height="24" viewBox="0 0 14 24"><polyline points="12,2 2,12 12,22" fill="none" stroke="#dc0a12" stroke-width="2.5"/></svg>
  <div class="abs partner" style="left:189px;width:66px"></div>
  <div class="abs partner" style="left:298px;width:130px"></div>
  <div class="abs partner" style="left:543px;width:76px"></div>
  <div class="abs partner" style="left:698px;width:118px"></div>
  <div class="abs partner" style="left:866px;width:144px"></div>
  <svg class="abs" style="left:1061px;top:3428px" width="14" height="24" viewBox="0 0 14 24"><polyline points="2,2 12,12 2,22" fill="none" stroke="#dc0a12" stroke-width="2.5"/></svg>
</section>

<footer>
  <nav class="abs foot-nav"><span class="on">Home</span><span>About Us</span><span>Services</span><span>Practitioners</span><span>Commentaries</span><span>Blog</span><span>Video</span><span>Contact Us</span></nav>
  <div class="abs brand" style="left:116px;top:3642px"><span class="brand-dot"></span><span class="brand-name">Amber Lantern Collective</span></div>
  <div class="abs social" style="left:917px;border-radius:50%"></div>
  <div class="abs social" style="left:987px"></div>
  <div class="abs social" style="left:1052px"></div>
  <div class="abs" style="left:1114px;top:3664px;font-size:13px">M1</div>
  <div class="abs copy">&copy; 2020 &nbsp;| &nbsp; www.amberlantern.example</div>
</footer>

</body>
</html>
```